A Flyer for a clinic/hospital waiting room to warn about patients that they must not abuse our staff

we need a flyer (text attached) with a background of a female nurse or medical doctor photo. I like the example photo where there are four headless satff lined up - something like this, indicating that we are a team and will not tolerate abuse
A4
the text will be over the photo.

Target Market(s)

patients who come to our clinic

Industry/Entity Type

medicine - urology

Colors
0054AA
0677BA
7BADD7
CADEEF
E8F1F8
0094D4
00A9DD
6FCCEA
C7EBF8
E9F6FB

Requirements
Must have
• a photo taking up the whole A4, and text over this. The photos I haev sent are just examples - I will need yo to source a photo
Nice to have
• Horizontal A4 and vertical A4 options. Please add our logo in small , in the bottom right corner

```html
<!DOCTYPE html>
<html lang="en">
<head>
<meta charset="utf-8">
<title>Zero-Tolerance Flyer</title>
<link rel="stylesheet" href="https://fonts.googleapis.com/css2?family=Open+Sans:wght@600;700;800&display=swap">
<style>
  :root {
    --navy: #0054AA;
    --deep: #1f3f9a;
    --panel: rgba(35, 60, 150, 0.86);
    --cyan: #00A9DD;
    --sky: #0094D4;
    --light: #6FCCEA;
    --mid: #0677BA;
    --ink: #3a3a3a;
    --white: #ffffff;
    --page: #eef3f8;
  }
  * { margin: 0; padding: 0; box-sizing: border-box; }
  html, body { width: 960px; height: 1200px; overflow: hidden; background: var(--page); }
  body { font-family: "Open Sans", Arial, sans-serif; color: var(--white); }

  .flyer { position: absolute; left: 56px; top: 0; width: 848px; height: 1200px; overflow: hidden; }

  .flyer__photo {
    position: absolute; inset: 0;
    background:
      linear-gradient(90deg, rgba(0,84,170,0.25) 0%, rgba(0,0,0,0) 30%, rgba(0,0,0,0) 70%, rgba(6,119,186,0.35) 100%),
      linear-gradient(170deg, var(--sky) 0%, var(--cyan) 35%, var(--light) 55%, var(--cyan) 75%, var(--mid) 100%);
  }

  .headline { position: absolute; left: 39px; top: 0; width: 770px; }
  .headline__top { background: var(--navy); height: 177px; padding: 19px 0 0 25px; }
  .headline__row { display: flex; align-items: center; height: 72px; }
  .headline__lead { font-weight: 800; font-size: 50px; letter-spacing: -0.5px; line-height: 1; margin-right: 14px; }
  .headline__mark {
    background: var(--white); color: var(--ink); font-weight: 800; font-size: 50px;
    letter-spacing: -0.5px; line-height: 72px; padding: 0 4px; white-space: nowrap;
  }
  .headline__mid { font-weight: 800; font-size: 72px; letter-spacing: -1px; line-height: 1; margin-top: 8px; white-space: nowrap; }
  .headline__bottom {
    background: var(--white); color: var(--navy); height: 89px; padding-left: 20px;
    font-weight: 800; font-size: 57px; line-height: 89px; white-space: nowrap;
  }

  .notice { position: absolute; left: 39px; width: 759px; background: var(--panel); padding: 14px 22px; font-weight: 700; font-size: 19.5px; line-height: 23px; }
  .notice p { text-align: justify; text-align-last: center; }
  .notice--first { top: 684px; height: 124px; }
  .notice--second { top: 826px; height: 155px; }
  .notice--second p + p { margin-top: 23px; }

  .definition { position: absolute; left: 39px; top: 1001px; width: 418px; height: 199px; background: var(--panel); padding: 10px 0 0 12px; }
  .definition__title { font-weight: 800; font-size: 19px; line-height: 22px; margin-bottom: 8px; }
  .definition__list { list-style: none; font-weight: 700; font-size: 13.2px; line-height: 18px; margin-left: -4px; }
  .definition__list li::before { content: "\27A4"; font-size: 9px; margin-right: 4px; vertical-align: 1px; }

  .brand { position: absolute; left: 459px; top: 1001px; width: 339px; height: 199px; background: var(--white); display: flex; align-items: center; justify-content: center; gap: 10px; }
  .brand__dot { width: 22px; height: 22px; border-radius: 50%; background: var(--navy); }
  .brand__name { color: var(--navy); font-weight: 700; font-size: 30px; letter-spacing: -0.5px; }
</style>
</head>
<body>
  <main class="flyer">
    <div class="flyer__photo" role="img" aria-label="Photo of medical staff in white coats and scrubs standing side by side with arms crossed, tinted blue"></div>

    <header class="headline">
      <div class="headline__top">
        <div class="headline__row">
          <span class="headline__lead">WE HAVE</span>
          <span class="headline__mark">ZERO-TOLERANCE</span>
        </div>
        <div class="headline__mid">FOR ANY FORM OF</div>
      </div>
      <div class="headline__bottom">AGGRESSIVE BEHAVIOUR</div>
    </header>

    <section class="notice notice--first">
      <p>If any of our staff feel intimidated in any way, we will always support them. Incidents will result in your immediate removal from the facility, termination of your relationship with the practice, and may result in prosecution.</p>
    </section>

    <section class="notice notice--second">
      <p>In all circumstances we will support any staff member who wishes to press charges against a perpetrator of aggressive behaviour.</p>
      <p>We take this stance because our staff work extremely hard in busy circumstances to help you and we will no longer tolerate any form of aggression or abuse.</p>
    </section>

    <section class="definition">
      <h2 class="definition__title">Aggressive behaviour (in-person<br>or on the telephone) is:</h2>
      <ul class="definition__list">
        <li>Verbal harassment</li>
        <li>Any verbal or physical confrontation</li>
        <li>Raising your voice or making unreasonable demands</li>
        <li>Abusive or intimidating behaviour</li>
        <li>Sexual or suggestive language or behaviour</li>
        <li>Making threats to our staff</li>
        <li>Swearing</li>
      </ul>
    </section>

    <footer class="brand">
      <span class="brand__dot"></span>
      <span class="brand__name">Riverbend Urology</span>
    </footer>
  </main>
</body>
</html>
```